Bookmark Design

We would like to design a book mark with logos of our two business and a quote.

One side with the quote "The first wealth is health" - Tobias Quill Harrow and the two logos.

The back side has the two logos with its respective phone numbers and a common address (this is to be advised to the winner of the project).

```html
<!DOCTYPE html>
<html lang="en">
<head>
<meta charset="utf-8">
<title>Bookmark – Brightwater Clinic &amp; Linden Dental</title>
<link href="https://fonts.googleapis.com/css2?family=Comic+Neue:wght@400;700&family=Montserrat:wght@600;700&display=swap" rel="stylesheet">
<style>
  :root {
    --blue: #0654a3;
    --green: #6ab366;
    --lime: #8cc63f;
    --grey: #5f5f5f;
    --ink: #2b2b2b;
    --white: #ffffff;
    --stage: #d9d9d9;
  }
  * { box-sizing: border-box; margin: 0; padding: 0; }
  html, body { width: 1200px; height: 1200px; overflow: hidden; }
  body { background: var(--stage); position: relative; font-family: "Montserrat", sans-serif; }

  .bookmark { position: absolute; top: 147px; width: 318px; height: 906px; overflow: hidden; }
  .bookmark--front { left: 253px; }
  .bookmark--back { left: 629px; }
  .bookmark__bg { position: absolute; inset: 0; width: 100%; height: 100%; }
  .abs { position: absolute; left: 0; width: 100%; text-align: center; }

  /* brand lockups */
  .brand-mark { position: absolute; left: 50%; transform: translateX(-50%); border-radius: 50%; }
  .brand-name { font-family: "Montserrat", sans-serif; font-weight: 700; line-height: 1.15; }

  .front .brand-mark--clinic { top: 64px; width: 106px; height: 106px; border: 4px solid var(--white); }
  .front .brand-name--clinic { top: 176px; color: var(--white); font-size: 22px; letter-spacing: .5px; }
  .front .brand-mark--dental { top: 700px; width: 20px; height: 20px; background: var(--white); }
  .front .brand-name--dental { top: 736px; color: var(--white); font-size: 30px; }

  .quote { font-family: "Comic Neue", sans-serif; font-weight: 700; }
  .quote__mark { font-size: 64px; line-height: 1; color: var(--lime); font-family: Georgia, serif; }
  .quote__open { top: 296px; }
  .quote__line { font-size: 57px; line-height: 60px; color: var(--blue); }
  .quote__text { top: 340px; }
  .quote__accent { color: var(--lime); }
  .quote__close { top: 530px; color: var(--blue); }
  .quote__author { top: 572px; font-family: "Comic Neue", sans-serif; font-size: 20px; color: #555; }

  .back .brand-mark--clinic { top: 114px; width: 128px; height: 128px; border: 4px solid var(--blue); }
  .back .brand-name--clinic { top: 256px; color: var(--blue); font-size: 24px; }
  .back .brand-mark--dental { top: 498px; width: 22px; height: 22px; background: var(--green); }
  .back .brand-name--dental { top: 532px; color: var(--green); font-size: 31px; }

  .divider { position: absolute; left: 52px; width: 214px; height: 12px; }
  .divider::before, .divider::after { content: ""; position: absolute; top: 6px; width: 94px; height: 1.5px; background: var(--green); }
  .divider::before { left: 0; }
  .divider::after { right: 0; }
  .divider svg { position: absolute; left: 50%; top: -6px; transform: translateX(-50%); }
  .divider--plain::before { width: 100%; }
  .divider--plain::after { display: none; }

  .address { font-weight: 700; font-size: 17.5px; line-height: 27px; color: var(--ink); }

  .phone { position: absolute; height: 40px; border-radius: 20px; display: flex; align-items: center; padding-left: 6px; gap: 8px; color: var(--white); font-weight: 700; }
  .phone--clinic { top: 421px; left: 50px; width: 219px; background: var(--blue); font-size: 22px; }
  .phone--dental { top: 747px; left: 52px; width: 220px; background: var(--green); font-size: 19px; }
  .phone__icon { width: 28px; height: 28px; border-radius: 50%; background: var(--white); display: flex; align-items: center; justify-content: center; }
</style>
</head>
<body>

<!-- Front -->
<section class="bookmark bookmark--front front">
  <svg class="bookmark__bg" viewBox="0 0 318 906" preserveAspectRatio="none">
    <rect width="318" height="906" fill="#ffffff"/>
    <path d="M0 0H318V217Q159 330 0 217Z" fill="var(--blue)"/>
    <path d="M0 691Q159 560 318 691V906H0Z" fill="var(--green)"/>
    <circle cx="159" cy="29" r="9" fill="#9a9a9a"/>
  </svg>
  <div class="brand-mark brand-mark--clinic"></div>
  <div class="abs brand-name brand-name--clinic">BRIGHTWATER<br>CLINIC</div>

  <div class="abs quote quote__mark quote__open">&ldquo;</div>
  <div class="abs quote quote__text">
    <div class="quote__line">The first</div>
    <div class="quote__line">wealth is</div>
    <div class="quote__line quote__accent">health</div>
  </div>
  <div class="abs quote quote__mark quote__close">&rdquo;</div>
  <div class="abs quote__author">Tobias Quill Harrow</div>

  <div class="brand-mark brand-mark--dental"></div>
  <div class="abs brand-name brand-name--dental">Linden Dental</div>
</section>

<!-- Back -->
<section class="bookmark bookmark--back back">
  <svg class="bookmark__bg" viewBox="0 0 318 906" preserveAspectRatio="none">
    <rect width="318" height="906" fill="var(--blue)"/>
    <polygon points="0,0 158,56 0,113" fill="var(--lime)"/>
    <polygon points="0,113 158,56 318,113 318,906 0,906" fill="#ffffff"/>
    <polygon points="0,794 160,849 318,906 0,906" fill="var(--green)"/>
    <polygon points="160,849 318,794 318,906" fill="var(--grey)"/>
    <circle cx="159" cy="30" r="9" fill="#9a9a9a"/>
  </svg>

  <div class="brand-mark brand-mark--clinic"></div>
  <div class="abs brand-name brand-name--clinic">BRIGHTWATER<br>CLINIC</div>

  <div class="divider" style="top:325px">
    <svg width="16" height="22" viewBox="0 0 16 22"><path d="M8 0C3.6 0 0 3.4 0 7.7 0 13 8 22 8 22s8-9 8-14.3C16 3.4 12.4 0 8 0Zm0 11a3.3 3.3 0 1 1 0-6.6A3.3 3.3 0 0 1 8 11Z" fill="var(--blue)"/></svg>
  </div>
  <div class="abs address" style="top:342px">18B Marlow Street<br>Northvale, VIC 3990</div>
  <div class="divider divider--plain" style="top:397px"></div>

  <div class="phone phone--clinic">
    <span class="phone__icon"><svg width="16" height="16" viewBox="0 0 24 24"><path d="M6.6 10.8a15.1 15.1 0 0 0 6.6 6.6l2.2-2.2a1 1 0 0 1 1-.25 11.4 11.4 0 0 0 3.6.57 1 1 0 0 1 1 1V20a1 1 0 0 1-1 1A17 17 0 0 1 3 4a1 1 0 0 1 1-1h3.5a1 1 0 0 1 1 1c0 1.25.2 2.45.57 3.57a1 1 0 0 1-.25 1Z" fill="var(--lime)"/></svg></span>
    03 9000 1234
  </div>

  <div class="brand-mark brand-mark--dental"></div>
  <div class="abs brand-name brand-name--dental">Linden Dental</div>

  <div class="divider" style="top:624px">
    <svg width="16" height="22" viewBox="0 0 16 22"><path d="M8 0C3.6 0 0 3.4 0 7.7 0 13 8 22 8 22s8-9 8-14.3C16 3.4 12.4 0 8 0Zm0 11a3.3 3.3 0 1 1 0-6.6A3.3 3.3 0 0 1 8 11Z" fill="var(--grey)"/></svg>
  </div>
  <div class="abs address" style="top:640px">18B Marlow St,<br>Northvale VIC 3990,<br>Australia</div>
  <div class="divider divider--plain" style="top:720px"></div>

  <div class="phone phone--dental">
    <span class="phone__icon"><svg width="16" height="16" viewBox="0 0 24 24"><path d="M6.6 10.8a15.1 15.1 0 0 0 6.6 6.6l2.2-2.2a1 1 0 0 1 1-.25 11.4 11.4 0 0 0 3.6.57 1 1 0 0 1 1 1V20a1 1 0 0 1-1 1A17 17 0 0 1 3 4a1 1 0 0 1 1-1h3.5a1 1 0 0 1 1 1c0 1.25.2 2.45.57 3.57a1 1 0 0 1-.25 1Z" fill="var(--grey)"/></svg></span>
    +61 3 9000 5678
  </div>
</section>

</body>
</html>
```